Note Cards for Clients

Hi - I need a design for simple flat note-cards and envelopes to use to send clients a written note in a professional manner. Please use my logo and color scheme.

Hi again- sorry for the miscommunication. I'd like to have note-cards 5x8 with envelopes as opposed to traditional stationary samples.

Thanks!

It Professional

```html
<!DOCTYPE html>
<html lang="en">
<head>
<meta charset="utf-8">
<title>Calder Wealth Partners – Note Card and Envelopes</title>
<link href="https://fonts.googleapis.com/css2?family=Sorts+Mill+Goudy&display=swap" rel="stylesheet">
<style>
  :root {
    --navy: #0d3a82;
    --paper: #ffffff;
    --paper-shade: #eef0f3;
    --backdrop: #1c1c1c;
    --serif: "Sorts Mill Goudy", Georgia, serif;
  }
  * { margin: 0; padding: 0; box-sizing: border-box; }
  html, body { width: 1200px; height: 1200px; overflow: hidden; }
  body { background: var(--backdrop); position: relative; font-family: var(--serif); }

  .open-envelope { position: absolute; left: 230px; top: 160px; width: 540px; height: 548px; }

  .sheet {
    position: absolute;
    background: var(--paper);
    box-shadow: 0 2px 6px rgba(0,0,0,0.45);
  }
  .sheet .stripe-wide,
  .sheet .stripe-thin {
    position: absolute; top: 0; bottom: 0; background: var(--navy);
  }
  .sheet .stripe-wide { left: 9px; width: 8px; }
  .sheet .stripe-thin { left: 20px; width: 5px; }

  .envelope-front { left: 581px; top: 406px; width: 539px; height: 337px; }
  .note-card { left: 301px; top: 674px; width: 540px; height: 339px; }

  .brand {
    position: absolute;
    display: flex; align-items: center; gap: 6px;
    color: var(--navy);
    font-family: var(--serif);
    white-space: nowrap;
  }
  .brand .brand-square { background: var(--navy); display: block; }
  .envelope-front .brand { left: 33px; top: 22px; font-size: 20px; }
  .envelope-front .brand-square { width: 26px; height: 26px; }
  .note-card .brand { left: 50%; transform: translateX(-50%); top: 18px; font-size: 16px; }
  .note-card .brand-square { width: 20px; height: 20px; }

  .recipient {
    position: absolute; left: 0; right: 0; top: 162px;
    text-align: center;
    color: var(--navy);
    font-size: 15px; line-height: 17px;
    padding-left: 50px;
  }
</style>
</head>
<body>

  <svg class="open-envelope" viewBox="0 0 540 548" aria-label="Open envelope with navy liner">
    <polygon points="0,210 270,0 540,210 540,548 0,548" fill="var(--paper)"/>
    <polygon points="26,205 270,42 530,208 270,313 20,212" fill="var(--navy)"/>
    <polygon points="20,212 270,313 530,208 540,210 540,548 0,548 0,210" fill="var(--paper)"/>
    <polyline points="20,530 270,320 520,530" fill="none" stroke="var(--paper-shade)" stroke-width="2"/>
    <rect x="10" y="196" width="8" height="352" fill="var(--navy)"/>
    <rect x="21" y="196" width="5" height="352" fill="var(--navy)"/>
  </svg>

  <section class="sheet envelope-front">
    <span class="stripe-wide"></span><span class="stripe-thin"></span>
    <div class="brand"><span class="brand-square"></span>Calder Wealth Partners</div>
    <address class="recipient" style="font-style:normal">
      Mr. Alan Porter<br>
      48 Maple Court<br>
      Fairview OR 97024
    </address>
  </section>

  <section class="sheet note-card">
    <span class="stripe-wide"></span><span class="stripe-thin"></span>
    <div class="brand"><span class="brand-square"></span>Calder Wealth Partners</div>
  </section>

</body>
</html>
```